Pipe Bursting Company Brochure

Need a tri-fold brochure on our company. We are a underground water replacement company that specializes in Trenchless replacement of water systems utilizing "Pipe Bursting" techniques and HDPE pipe materials that come with a 50 year warranty on material and labot.

```html
<!DOCTYPE html>
<html lang="en">
<head>
<meta charset="utf-8">
<title>Trenchline – Pipe Bursting Tri-fold Brochure</title>
<link href="https://fonts.googleapis.com/css2?family=Roboto+Condensed:wght@400;700&family=Open+Sans:wght@400;600;700&display=swap" rel="stylesheet">
<style>
:root{
  --blue:#1f56a8;
  --blue-dark:#133b7a;
  --blue-light:#3f7fd0;
  --ink:#222831;
  --text:#4a4f57;
  --paper:#ffffff;
  --band:#111316;
  --red:#c8242c;
  --stage:#e4e4e4;
}
*{box-sizing:border-box;margin:0;padding:0}
html,body{width:1200px;height:2400px;overflow:hidden}
body{background:var(--stage);font-family:"Open Sans",Arial,sans-serif;color:var(--text);position:relative}

.spread{position:absolute;left:40px;width:1120px;height:867px;display:grid;grid-template-columns:repeat(3,1fr);box-shadow:0 10px 30px rgba(0,0,0,.18);background:var(--paper)}
.spread--outside{top:273px}
.spread--inside{top:1260px}

.panel{position:relative;overflow:hidden;background:var(--paper);border-right:1px solid #e2e4e8}
.panel:last-child{border-right:0}
.panel--blue{background:linear-gradient(180deg,var(--blue) 0%,var(--blue-dark) 100%);color:#fff}

.panel-footer{position:absolute;left:0;right:0;bottom:0;height:64px}
.panel-footer .phone{position:absolute;left:0;right:0;top:4px;height:26px;display:flex;align-items:center;justify-content:center;gap:8px;font:700 14px "Roboto Condensed",Arial,sans-serif;color:var(--ink);letter-spacing:.5px}
.panel--blue .panel-footer .phone{background:#fff;color:var(--ink)}
.panel-footer svg.band{position:absolute;left:0;bottom:0;width:100%;height:30px}
.phone svg{width:14px;height:14px}

.photo{position:absolute;left:0;right:0}
.photo--burst{background:radial-gradient(ellipse at 55% 45%,#8a7a68 0%,#4b4540 35%,#1c1c1d 75%)}
.photo--plans{background:linear-gradient(135deg,#dfe9f3 0%,#a8c2dc 50%,#6e8fb3 100%)}
.photo--screens{background:linear-gradient(135deg,#1a1d22,#33404f)}
.photo--rusty{background:radial-gradient(circle at 40% 55%,#c9c6c1 0%,#8d6a4d 40%,#5a3a24 80%)}
.photo--tubes{background:radial-gradient(circle at 50% 50%,#5aa3ee 0%,#1f63c4 50%,#0c2f6b 100%)}

.swoosh{position:absolute;left:0;width:100%}

.brand{display:flex;align-items:center;gap:12px}
.brand-dot{width:34px;height:34px;border-radius:50%;background:var(--blue)}
.brand-name{font:700 40px "Roboto Condensed",Arial,sans-serif;color:var(--blue);letter-spacing:1px}
.panel--blue .brand-dot{background:#fff}
.panel--blue .brand-name{color:#fff}

.cover-brand{position:absolute;top:72px;right:34px}
.cover-brand .brand{justify-content:flex-end}
.steps{position:absolute;top:590px;left:0;right:0;display:flex;justify-content:center;gap:38px}
.step{display:flex;flex-direction:column;align-items:center;gap:8px}
.step-icon{width:62px;height:62px;border-radius:50%;background:var(--blue);border:4px solid #fff;box-shadow:0 0 0 2px var(--blue);display:flex;align-items:center;justify-content:center}
.step-icon svg{width:32px;height:32px}
.step-label{font:700 15px "Roboto Condensed",Arial,sans-serif;color:var(--ink);text-transform:uppercase;letter-spacing:.5px}
.cover-title{position:absolute;top:715px;left:0;right:0;text-align:center}
.cover-title h1{font:700 44px/1 "Roboto Condensed",Arial,sans-serif;color:var(--blue);letter-spacing:1px;text-transform:uppercase}
.cover-title p{font:700 16px "Roboto Condensed",Arial,sans-serif;color:var(--ink);margin-top:8px;text-transform:uppercase;letter-spacing:.4px}

.copy{position:absolute;left:28px;right:28px}
.copy h2{font:700 17px/1.2 "Roboto Condensed",Arial,sans-serif;color:var(--blue);text-transform:uppercase;letter-spacing:.4px;margin:0 0 8px}
.copy h3{font:700 12px/1.25 "Roboto Condensed",Arial,sans-serif;color:var(--ink);text-transform:uppercase;margin:-4px 0 8px}
.copy p{font-size:11.5px;line-height:1.6;margin-bottom:10px}
.copy section{margin-bottom:16px}
.panel--blue .copy h2{color:#fff;text-align:center}
.panel--blue .copy p{color:#e3ecf8;text-align:center}

.seal{position:absolute;top:28px;left:50%;margin-left:-62px;width:124px;height:124px;border-radius:50%;background:var(--red);border:6px solid #fff;box-shadow:0 0 0 2px var(--red)}
.blue-brand{position:absolute;top:200px;left:0;right:0}
.blue-brand .brand{justify-content:center}
.partner{position:absolute;top:640px;left:0;right:0;display:flex;align-items:center;justify-content:center;gap:10px}
.partner-mark{width:38px;height:38px;border-radius:50%;background:#fff}
.partner-name{font:700 18px "Roboto Condensed",Arial,sans-serif;color:#fff}
.web{position:absolute;top:735px;left:40px;right:40px;height:26px;border-radius:13px;background:#fff;color:var(--ink);font:600 12px "Open Sans",Arial,sans-serif;display:flex;align-items:center;justify-content:center}
</style>
</head>
<body>

<main class="spread spread--outside">

  <article class="panel">
    <div class="photo photo--plans" style="top:0;height:230px" role="img" aria-label="Engineers reviewing construction plans on a desk"></div>
    <svg class="swoosh" style="top:190px;height:70px" viewBox="0 0 373 70" preserveAspectRatio="none">
      <path d="M0 40 Q190 0 373 20 L373 70 L0 70Z" fill="#fff"/>
      <path d="M0 40 Q190 0 373 20" stroke="var(--blue)" stroke-width="5" fill="none"/>
    </svg>
    <div class="copy" style="top:272px">
      <h2>Quality Control</h2>
      <p>Our installation team takes great pride in the quality of every replacement project. Each length of pipe is inspected on arrival, tracked through fusion and tested after installation so the finished line meets the standard we promise.</p>
      <p>During production, the pipe is checked at every stage for wall thickness, diameter and strength. Fusion joints are logged and pressure tested before the system is returned to service.</p>
      <p>Our pipe supplier operates a certified quality management system, and every crew member is trained to follow the same written procedures on site.</p>
    </div>
    <div class="panel-footer">
      <div class="phone"><svg viewBox="0 0 24 24"><path d="M6.6 10.8a15 15 0 006.6 6.6l2.2-2.2a1 1 0 011-.25 11.4 11.4 0 003.6.6 1 1 0 011 1V20a1 1 0 01-1 1A17 17 0 013 4a1 1 0 011-1h3.5a1 1 0 011 1 11.4 11.4 0 00.6 3.6 1 1 0 01-.25 1z" fill="currentColor"/></svg>(555) 014-3547</div>
      <svg class="band" viewBox="0 0 373 30" preserveAspectRatio="none"><rect y="8" width="373" height="22" fill="var(--band)"/><path d="M300 8 L316 8 L296 30 L280 30Z" fill="var(--blue)"/><path d="M322 8 L330 8 L310 30 L302 30Z" fill="var(--blue-light)"/></svg>
    </div>
  </article>

  <article class="panel panel--blue">
    <div class="seal" role="img" aria-label="Warranty seal"></div>
    <div class="blue-brand">
      <div class="brand"><span class="brand-dot"></span><span class="brand-name">Trenchline</span></div>
    </div>
    <div class="copy" style="top:330px">
      <h2>What Do We Do?</h2>
      <p>We replace your old pipes that have either rusted or worn with new HDPE pipe. This does all of your water lines so your water will flow more freely and your property stays dry.</p>
      <p>We offer free consultations and special financing for approved customers. Please call us today to schedule an appointment and you can start saving money now!</p>
    </div>
    <div class="partner"><span class="partner-mark"></span><span class="partner-name">Summit Pipe Co.</span></div>
    <div class="web">trenchline-pipe.example</div>
    <div class="panel-footer">
      <div class="phone"><svg viewBox="0 0 24 24"><path d="M6.6 10.8a15 15 0 006.6 6.6l2.2-2.2a1 1 0 011-.25 11.4 11.4 0 003.6.6 1 1 0 011 1V20a1 1 0 01-1 1A17 17 0 013 4a1 1 0 011-1h3.5a1 1 0 011 1 11.4 11.4 0 00.6 3.6 1 1 0 01-.25 1z" fill="currentColor"/></svg>(555) 014-8425</div>
      <svg class="band" viewBox="0 0 373 30" preserveAspectRatio="none"><rect y="8" width="373" height="22" fill="var(--band)"/><path d="M300 8 L316 8 L296 30 L280 30Z" fill="var(--blue)"/><path d="M322 8 L330 8 L310 30 L302 30Z" fill="var(--blue-light)"/></svg>
    </div>
  </article>

  <article class="panel">
    <div class="cover-brand">
      <div class="brand"><span class="brand-dot"></span><span class="brand-name">Trenchline</span></div>
    </div>
    <div class="photo photo--burst" style="top:170px;height:420px" role="img" aria-label="Old water main bursting underground with water spraying"></div>
    <svg class="swoosh" style="top:160px;height:50px" viewBox="0 0 373 50" preserveAspectRatio="none">
      <path d="M0 0 L373 0 L373 10 Q180 50 0 20Z" fill="#fff"/>
      <path d="M0 20 Q180 50 373 10" stroke="var(--blue)" stroke-width="6" fill="none"/>
    </svg>
    <svg class="swoosh" style="top:540px;height:60px" viewBox="0 0 373 60" preserveAspectRatio="none">
      <path d="M0 15 Q200 55 373 30 L373 60 L0 60Z" fill="#fff"/>
      <path d="M0 15 Q200 55 373 30" stroke="var(--blue)" stroke-width="6" fill="none"/>
    </svg>
    <div class="steps">
      <div class="step">
        <span class="step-icon"><svg viewBox="0 0 32 32"><circle cx="13" cy="13" r="8" stroke="#fff" stroke-width="3" fill="none"/><path d="M19 19l8 8" stroke="#fff" stroke-width="4" stroke-linecap="round"/></svg></span>
        <span class="step-label">Investigate</span>
      </div>
      <div class="step">
        <span class="step-icon"><svg viewBox="0 0 32 32"><rect x="7" y="6" width="18" height="22" rx="2" stroke="#fff" stroke-width="2.5" fill="none"/><path d="M11 13h10M11 18h10M11 23h6" stroke="#fff" stroke-width="2.5"/></svg></span>
        <span class="step-label">Plan</span>
      </div>
      <div class="step">
        <span class="step-icon"><svg viewBox="0 0 32 32"><rect x="4" y="12" width="20" height="9" fill="#fff"/><rect x="23" y="10" width="5" height="13" fill="#fff"/></svg></span>
        <span class="step-label">Deliver</span>
      </div>
    </div>
    <div class="cover-title">
      <h1>Pipe Bursting</h1>
      <p>HDPE Pipe Materials with a 50 Year Warranty</p>
    </div>
    <div class="panel-footer">
      <div class="phone"><svg viewBox="0 0 24 24"><path d="M6.6 10.8a15 15 0 006.6 6.6l2.2-2.2a1 1 0 011-.25 11.4 11.4 0 003.6.6 1 1 0 011 1V20a1 1 0 01-1 1A17 17 0 013 4a1 1 0 011-1h3.5a1 1 0 011 1 11.4 11.4 0 00.6 3.6 1 1 0 01-.25 1z" fill="currentColor"/></svg>(555) 014-3152</div>
      <svg class="band" viewBox="0 0 373 30" preserveAspectRatio="none"><rect y="8" width="373" height="22" fill="var(--band)"/><path d="M300 8 L316 8 L296 30 L280 30Z" fill="var(--blue)"/><path d="M322 8 L330 8 L310 30 L302 30Z" fill="var(--blue-light)"/></svg>
    </div>
  </article>
</main>

<main class="spread spread--inside">

  <article class="panel">
    <div class="photo photo--screens" style="top:0;height:250px" role="img" aria-label="Four step diagram of the pipe bursting process"></div>
    <svg class="swoosh" style="top:215px;height:60px" viewBox="0 0 373 60" preserveAspectRatio="none">
      <path d="M0 35 Q190 0 373 25 L373 60 L0 60Z" fill="#fff"/>
      <path d="M0 35 Q190 0 373 25" stroke="var(--blue)" stroke-width="5" fill="none"/>
    </svg>
    <div class="copy" style="top:290px">
      <section>
        <h2>High-Density Poly Ethylene Water and Sewer Pipe</h2>
        <h3>For municipal and industrial water and sewer piping systems</h3>
        <p>Our supplier manufactures high-density polyethylene pressure pipe for municipal and industrial water transmission systems, available in a wide range of sizes.</p>
        <p>HDPE pipe is recognized for its leak-free joints, high performance and long life expectancy. It can be produced with color striping to identify potable water, sewer or reclaimed water lines.</p>
      </section>
      <section>
        <h2>Corrosion Resistance</h2>
        <p>HDPE pipe has excellent resistance against electrolytic or galvanic corrosion in any known soil or water condition. You will never worry about tuberculation, coating or cathodic protection.</p>
      </section>
    </div>
    <div class="panel-footer">
      <div class="phone"><svg viewBox="0 0 24 24"><path d="M6.6 10.8a15 15 0 006.6 6.6l2.2-2.2a1 1 0 011-.25 11.4 11.4 0 003.6.6 1 1 0 011 1V20a1 1 0 01-1 1A17 17 0 013 4a1 1 0 011-1h3.5a1 1 0 011 1 11.4 11.4 0 00.6 3.6 1 1 0 01-.25 1z" fill="currentColor"/></svg>(555) 014-3547</div>
      <svg class="band" viewBox="0 0 373 30" preserveAspectRatio="none"><rect y="8" width="373" height="22" fill="var(--blue)"/><path d="M300 8 L316 8 L296 30 L280 30Z" fill="var(--band)"/></svg>
    </div>
  </article>

  <article class="panel">
    <div class="photo photo--rusty" style="top:0;height:250px" role="img" aria-label="Corroded old pipe beside new pipe, before and after comparison"></div>
    <svg class="swoosh" style="top:215px;height:60px" viewBox="0 0 373 60" preserveAspectRatio="none">
      <path d="M0 25 Q190 0 373 35 L373 60 L0 60Z" fill="#fff"/>
      <path d="M0 25 Q190 0 373 35" stroke="var(--blue)" stroke-width="5" fill="none"/>
    </svg>
    <div class="copy" style="top:290px">
      <section>
        <h2>Installation Design</h2>
        <p>HDPE pipe provides efficient installation, utilizing the proven trenchless method of pipe bursting. The old line is split and pushed aside while the new pipe is pulled into place behind it.</p>
        <p>Mechanical connections can be applied at each end, so the new line ties directly into your existing fittings without major excavation of your yard.</p>
      </section>
      <section>
        <h2>Long Laying Lengths</h2>
        <p>The standard laying length of HDPE pressure pipe is fifty feet, and lengths are fused together on site, reducing the number of joints and the labor needed.</p>
      </section>
      <section>
        <h2>Applicable Specifications</h2>
        <p>Our HDPE pressure pipe is manufactured in accordance with recognized national water works and testing standards, and is certified for potable water.</p>
      </section>
    </div>
    <div class="panel-footer">
      <div class="phone"><svg viewBox="0 0 24 24"><path d="M6.6 10.8a15 15 0 006.6 6.6l2.2-2.2a1 1 0 011-.25 11.4 11.4 0 003.6.6 1 1 0 011 1V20a1 1 0 01-1 1A17 17 0 013 4a1 1 0 011-1h3.5a1 1 0 011 1 11.4 11.4 0 00.6 3.6 1 1 0 01-.25 1z" fill="currentColor"/></svg>(555) 014-8425</div>
      <svg class="band" viewBox="0 0 373 30" preserveAspectRatio="none"><rect y="8" width="373" height="22" fill="var(--blue)"/><path d="M300 8 L316 8 L296 30 L280 30Z" fill="var(--band)"/></svg>
    </div>
  </article>

  <article class="panel">
    <div class="photo photo--tubes" style="top:0;height:250px" role="img" aria-label="Stacked blue HDPE pipes seen end-on"></div>
    <svg class="swoosh" style="top:215px;height:60px" viewBox="0 0 373 60" preserveAspectRatio="none">
      <path d="M0 35 Q190 0 373 25 L373 60 L0 60Z" fill="#fff"/>
      <path d="M0 35 Q190 0 373 25" stroke="var(--blue)" stroke-width="5" fill="none"/>
    </svg>
    <div class="copy" style="top:290px">
      <section>
        <h2>Flow Capacity</h2>
        <p>HDPE pipe has a smooth interior surface that stays smooth for the life of the line. It will not build up scale, so the flow capacity you have on day one is the flow you keep for decades.</p>
      </section>
      <section>
        <h2>Materials</h2>
        <p>HDPE water pipe is manufactured from high quality resin that is tough, flexible and durable. It resists impact and ground movement and is backed by a fifty year warranty.</p>
      </section>
      <section>
        <h2>Reduced Installation Cost</h2>
        <p>HDPE is lightweight, flexible and fused in long lengths. Trenchless installation means less digging, less restoration and a lower total project cost for you.</p>
      </section>
    </div>
    <div class="panel-footer">
      <div class="phone"><svg viewBox="0 0 24 24"><path d="M6.6 10.8a15 15 0 006.6 6.6l2.2-2.2a1 1 0 011-.25 11.4 11.4 0 003.6.6 1 1 0 011 1V20a1 1 0 01-1 1A17 17 0 013 4a1 1 0 011-1h3.5a1 1 0 011 1 11.4 11.4 0 00.6 3.6 1 1 0 01-.25 1z" fill="currentColor"/></svg>(555) 014-3152</div>
      <svg class="band" viewBox="0 0 373 30" preserveAspectRatio="none"><rect y="8" width="373" height="22" fill="var(--blue)"/><path d="M300 8 L316 8 L296 30 L280 30Z" fill="var(--band)"/></svg>
    </div>
  </article>
</main>

</body>
</html>
```